Webdesign für K&L Vendora GmbH
Zielgruppe
- Partner für moderne Automaten- und Verpflegungslösungen in Unternehmen
- Zielgruppe sind Unternehmen, welche Versorgungskonzepte schaffen, die optimal auf die Bedürfnisse von Mitarbeitenden, Kunden und Gästen abgestimmt sind
Aufgabenstellung
- KEINE Kopie der alten Webseite
- Farbkonzept gern in sanften Kaffeetönen kombiniert mit Weiß
- Klare Struktur der Webseite

```html
<!DOCTYPE html>
<html lang="de">
<head>
<meta charset="utf-8">
<title>K&amp;L Vendora GmbH – Automatenlösungen</title>
<link href="https://fonts.googleapis.com/css2?family=Rubik:wght@600;700&family=Inter:wght@400;500&display=swap" rel="stylesheet">
<style>
  :root{
    --navy:#13235f;
    --accent:#6f96d1;
    --band:#7098d1;
    --band-text:#eef3fb;
    --text:#1a1f2e;
    --page:#ffffff;
    --outside:#f4f4f5;
    --icon-fill:#e8eef8;
  }
  *{box-sizing:border-box;margin:0;padding:0}
  html,body{width:1200px;height:1200px;overflow:hidden}
  body{background:var(--outside);font-family:"Inter",sans-serif;color:var(--text);position:relative}
  .page{position:absolute;left:75px;top:0;width:1058px;height:1200px;background:var(--page);box-shadow:0 0 30px rgba(0,0,0,.08);overflow:hidden}
  .abs{position:absolute}
  .hero-circle{left:173px;top:-160px;width:180px;height:180px;border-radius:50%;background:var(--accent)}
  .hero-machine{left:298px;top:-10px;width:137px;height:53px;background:linear-gradient(#3a2d24,#111);border-radius:0 0 4px 4px}
  .checks{list-style:none}
  .checks li{position:relative;padding-left:17px;white-space:nowrap}
  .checks li::before{content:"✔";position:absolute;left:0;top:0;color:var(--accent);font-size:.8em}
  .hero-checks{left:544px;top:0;font-size:13.7px;line-height:22px}
  .card{width:168px;height:245px;top:110px;background:#fff;border-radius:18px;box-shadow:0 4px 16px rgba(19,35,95,.12);text-align:center}
  .card-icon{position:absolute;left:50%;top:28px;width:70px;height:96px;transform:translateX(-50%);border-radius:6px;background:var(--icon-fill)}
  .card-icon.narrow{width:40px;height:102px}
  .card h3{position:absolute;left:0;right:0;font-family:"Rubik",sans-serif;font-weight:700;color:var(--navy);font-size:16.5px;line-height:18px}
  .card p{position:absolute;left:10px;right:10px;font-size:11px;line-height:12.5px;color:var(--navy)}
  .section-title{font-family:"Rubik",sans-serif;font-weight:700;color:var(--navy);font-size:32px;letter-spacing:-.3px;white-space:nowrap}
  .rule{height:3px;width:36px;background:var(--accent)}
  .lead{left:74px;top:555px;width:470px;font-size:15px;line-height:22px}
  .benefits{left:74px;top:665px;font-size:15px;line-height:22px}
  .photo{left:590px;top:429px;width:468px;height:376px;border-radius:16px 0 0 16px;
    background:
      radial-gradient(ellipse 55% 40% at 35% 90%, rgba(226,206,178,.85), rgba(226,206,178,0) 70%),
      radial-gradient(ellipse 30% 45% at 55% 40%, rgba(178,72,52,.45), rgba(178,72,52,0) 70%),
      linear-gradient(100deg,#e4d6c2 0%,#9a8573 16%,#45403f 34%,#2b2b31 60%,#1c1d22 100%)}
  .brand-badge{left:533px;top:670px;width:100px;height:100px;border-radius:50%;background:#edf1f8;box-shadow:0 4px 14px rgba(0,0,0,.15);display:flex;align-items:center;justify-content:center;text-align:center;font-family:"Rubik",sans-serif;font-weight:700;color:var(--navy);font-size:15px;line-height:17px}
  .band{left:0;top:853px;width:1058px;height:228px;background:var(--band);text-align:center}
  .band h2{font-family:"Rubik",sans-serif;font-weight:700;color:#fff;font-size:28px;line-height:34px;margin-top:40px}
  .band p{margin:18px auto 0;width:800px;font-size:15px;line-height:22px;color:var(--band-text)}
</style>
</head>
<body>
<main class="page">
  <div class="abs hero-circle"></div>
  <div class="abs hero-machine" role="img" aria-label="Foto eines Kaffeevollautomaten"></div>
  <ul class="abs checks hero-checks">
    <li>Wasserspender für Büros, Produktionsstätten und Empfangsbereiche</li>
    <li>Moderne Bezahlsysteme und individuelle Ausstattungsoptionen</li>
  </ul>

  <article class="abs card" style="left:60px">
    <div class="card-icon" role="img" aria-label="Illustration eines Standautomaten"></div>
    <h3 style="top:148px">Standgeräte</h3>
    <p style="top:187px">flexible Lösungen<br>für verschiedene<br>Einsatzbereiche</p>
  </article>
  <article class="abs card" style="left:253px">
    <div class="card-icon" role="img" aria-label="Illustration eines Heißgetränkeautomaten"></div>
    <h3 style="top:148px">InCup-Systeme</h3>
    <p style="top:187px">schnelle, saubere und<br>praktische<br>Getränkezubereitung</p>
  </article>
  <article class="abs card" style="left:445px">
    <div class="card-icon" role="img" aria-label="Illustration eines Kaltgetränkeautomaten"></div>
    <h3 style="top:142px">Kaltgetränke<br>Automaten</h3>
    <p style="top:184px">gekühlte Erfrischungen<br>jederzeit verfügbar</p>
  </article>
  <article class="abs card" style="left:638px">
    <div class="card-icon" role="img" aria-label="Illustration eines Snackautomaten"></div>
    <h3 style="top:142px">Snack<br>Automaten</h3>
    <p style="top:184px">schnelle Verpflegung<br>für zwischendurch</p>
  </article>
  <article class="abs card" style="left:830px">
    <div class="card-icon narrow" role="img" aria-label="Illustration eines Wasserspenders"></div>
    <h3 style="top:151px">Wasserspender</h3>
    <p style="top:189px">frisches Trinkwasser<br>für Büro &amp; Betrieb</p>
  </article>

  <h2 class="abs section-title" style="left:74px;top:450px">Alles aus einer Hand</h2>
  <div class="abs rule" style="left:73px;top:502px"></div>
  <p class="abs lead">Von der persönlichen Beratung über die Installation bis hin zur regelmäßigen Wartung und Befüllung Ihrer Automaten kümmern wir uns um den kompletten Betrieb.</p>
  <ul class="abs checks benefits">
    <li>Individuelle Beratung vor Ort</li>
    <li>Zuverlässiger Kundenservice in Sachsen</li>
    <li>Moderne, leistungsstarke Geräte</li>
    <li>Flexible und wirtschaftliche Konzepte</li>
  </ul>
  <div class="abs photo" role="img" aria-label="Foto: Hand wählt an einem Snackautomaten mit Tastenfeld und Display ein Produkt"></div>
  <div class="abs brand-badge">K&amp;L<br>Vendora</div>

  <section class="abs band">
    <h2>Warum K&amp;L Vendora?</h2>
    <p>Als regionaler Anbieter stehen wir für Qualität, Zuverlässigkeit und persönlichen Service. Unsere Lösungen<br>sorgen für zufriedene Mitarbeitende und einen professionellen Eindruck bei Ihren Kunden.<br>Entscheiden Sie sich für Getränke- und Snackautomaten in Chemnitz – mit einem Partner, der Ihre<br>Anforderungen versteht.</p>
  </section>

  <h2 class="abs section-title" style="left:74px;top:1132px">Wir freuen uns auf Ihre Anfrage</h2>
  <div class="abs rule" style="left:74px;top:1180px"></div>
</main>
</body>
</html>
```